Tello Haulage Junk Removal Postcard

I am looking to have a postcard made for my junk removal company. Details:
size: 6"x9"
I would like to keep it clean and simple. Our company colors are pink, blue and white. You can find the colors and info on the company and what we do on our website which is www.tellohaulage.example .
I've attached a sample of a postcard that was made on ArtHive for another junk removal company. I like the way the attached one looks.

```html
<!DOCTYPE html>
<html lang="en">
<head>
<meta charset="utf-8">
<title>Tello Haulage Postcard</title>
<link href="https://fonts.googleapis.com/css2?family=Jost:wght@400;500;600;700;800&display=swap" rel="stylesheet">
<style>
:root{
  --pink:#e5067f;
  --pink-soft:#e12d9a;
  --blue:#0a5fad;
  --ink:#0a0a0a;
  --white:#ffffff;
  --page:#d9d9d9;
  --rule:#c4c4c4;
}
*{margin:0;padding:0;box-sizing:border-box}
html,body{width:1200px;height:1200px;overflow:hidden;background:var(--page);font-family:"Jost",sans-serif}
.postcard{position:absolute;background:var(--white);overflow:hidden}
.postcard svg.shapes{position:absolute;left:0;top:0;width:100%;height:100%}
.front{left:230px;top:52px;width:741px;height:494px}
.back{left:212px;top:614px;width:759px;height:506px}
.abs{position:absolute;white-space:nowrap}

.brand{right:38px;top:34px;display:flex;align-items:center;gap:6px;font-weight:700;font-size:17px;color:var(--blue)}
.brand .dot{width:12px;height:12px;border-radius:50%;background:var(--pink)}
.kicker{right:39px;top:104px;font-weight:700;font-size:28px;color:var(--ink);letter-spacing:.5px}
.headline{right:36px;top:136px;text-align:right;font-weight:800;font-size:41px;line-height:45px;color:var(--ink);letter-spacing:.6px}
.blurb{left:451px;top:236px;font-weight:700;font-size:16.6px;line-height:20.6px;color:var(--ink);letter-spacing:.2px}
.contact{left:388px;top:381px;color:var(--white);font-weight:700;font-size:20.5px;line-height:25px}
.contact div{display:flex;align-items:center;gap:8px}
.contact svg{width:15px;height:15px;flex:none}
.social{right:21px;top:443px;display:flex;align-items:center;gap:6px;font-weight:600;font-size:11px;color:var(--blue)}
.social .dot{width:21px;height:21px;border-radius:50%;background:var(--blue)}

.services-title{left:30px;top:31px;font-weight:800;font-size:31px;color:var(--white);letter-spacing:.5px}
.services{left:30px;top:76px;list-style:none;color:var(--white);font-weight:700;font-size:25.5px}
.services li{display:flex;align-items:center;gap:10px;height:35px}
.services svg{width:17px;height:17px;flex:none}
.band-title{font-weight:800;font-size:28px;letter-spacing:.3px}
.clean{left:26px;top:242px;color:var(--white)}
.others{left:28px;top:287px;color:var(--ink)}
.more{left:25px;top:337px;font-size:14.3px;line-height:17px;color:var(--white)}
.extras{left:25px;top:394px;list-style:none;color:var(--white);font-size:17.6px}
.extras li{height:24.6px;line-height:22px}
.extras li::before{content:"\2022";margin-right:6px;font-size:15px}
.estimate{left:500px;top:382px;font-weight:800;font-size:31px;line-height:46px;color:var(--white);letter-spacing:.6px}
</style>
</head>
<body>

<section class="postcard front">
  <svg class="shapes" viewBox="0 0 1194 796" preserveAspectRatio="none">
    <defs>
      <linearGradient id="truckScene" x1="0" y1="0" x2="0" y2="1">
        <stop offset="0" stop-color="#3d7fd1"/>
        <stop offset=".45" stop-color="#c9ccd4"/>
        <stop offset=".8" stop-color="#2b2a35"/>
        <stop offset="1" stop-color="#1c1a22"/>
      </linearGradient>
    </defs>
    <polygon points="0,0 90,0 50,76 0,76" fill="var(--pink)"/>
    <polygon points="90,0 796,0 600,370 0,370" fill="var(--blue)"/>
    <polygon points="560,420 615,486 798,796 0,796 0,450" fill="var(--pink)"/>
    <polygon points="0,754 383,754 372,773 0,773" fill="var(--blue)"/>
    <polygon points="0,76 460,76 652,413 462,753 0,753" fill="url(#truckScene)" role="img" aria-label="Photo of the company's white box truck parked in a driveway with a crew member beside the cab"/>
    <polygon points="975,583 1194,583 1194,604 963,604" fill="var(--pink-soft)"/>
    <polygon points="605,604 1194,604 1194,701 560,701" fill="var(--blue)"/>
  </svg>

  <div class="abs brand"><span class="dot"></span>Tello Haulage</div>
  <p class="abs kicker">RELAX</p>
  <h1 class="abs headline">WE DO THE<br>DIRTY WORK</h1>
  <p class="abs blurb">Junk, clutter, debris, rubbish,<br>trash, hogwash, garbage and<br>scrap.whatever you’re under,<br>we’re here to help clean it out.</p>
  <div class="abs contact">
    <div><svg viewBox="0 0 16 16"><rect x="1" y="3" width="14" height="10" rx="1" fill="#fff"/><path d="M1.5 3.8 8 9l6.5-5.2" stroke="var(--blue)" stroke-width="1.4" fill="none"/></svg>info@tellohaulage.example</div>
    <div><svg viewBox="0 0 16 16"><path d="M3 1.5l2.6 0 1.2 3.3-1.6 1.2c.9 1.9 2.2 3.2 4.1 4.1l1.2-1.6 3.3 1.2v2.6c0 .9-.8 1.6-1.7 1.5C6.5 13.2 2.8 9.5 1.5 3.2 1.4 2.3 2.1 1.5 3 1.5z" fill="#fff"/></svg>555-284-0193</div>
  </div>
  <div class="abs social">tellohaulage<span class="dot"></span></div>
</section>

<section class="postcard back">
  <svg class="shapes" viewBox="0 0 1222 814" preserveAspectRatio="none">
    <defs>
      <linearGradient id="junkScene" x1="0" y1="0" x2="0" y2="1">
        <stop offset="0" stop-color="#c9b9a6"/>
        <stop offset=".4" stop-color="#4a5a4c"/>
        <stop offset=".75" stop-color="#2a4a3a"/>
        <stop offset="1" stop-color="#3a3d44"/>
      </linearGradient>
    </defs>
    <rect x="0" y="0" width="655" height="392" fill="var(--pink)"/>
    <polygon points="0,391 345,391 375,449 0,449" fill="var(--blue)"/>
    <polygon points="0,449 410,449 410,518 0,518" fill="var(--pink)"/>
    <polygon points="0,463 306,463 343,518 0,518" fill="var(--white)"/>
    <polygon points="409,166 655,166 655,518 409,518 309,341" fill="url(#junkScene)" stroke="var(--white)" stroke-width="6" role="img" aria-label="Photo of a curbside junk pile with a green trash bin, furniture and bags"/>
    <polygon points="0,518 742,518 927,814 0,814" fill="var(--blue)"/>
    <polygon points="1009,586 1222,586 1222,606 997,606" fill="var(--blue)"/>
    <polygon points="799,606 1222,606 1222,694 745,694" fill="var(--pink-soft)"/>
    <rect x="1061" y="56" width="108" height="103" fill="none" stroke="var(--rule)" stroke-width="2"/>
    <line x1="773" y1="209" x2="1169" y2="209" stroke="var(--rule)" stroke-width="2"/>
    <line x1="773" y1="256" x2="1169" y2="256" stroke="var(--rule)" stroke-width="2"/>
    <line x1="773" y1="311" x2="1169" y2="311" stroke="var(--rule)" stroke-width="2"/>
  </svg>

  <h2 class="abs services-title">OUR SERVICES</h2>
  <ul class="abs services">
    <li><svg viewBox="0 0 20 20"><circle cx="10" cy="10" r="8" fill="none" stroke="var(--blue)" stroke-width="2"/><path d="M6 10l3 3 6-6" fill="none" stroke="var(--blue)" stroke-width="2"/></svg>Residential</li>
    <li><svg viewBox="0 0 20 20"><circle cx="10" cy="10" r="8" fill="none" stroke="var(--blue)" stroke-width="2"/><path d="M6 10l3 3 6-6" fill="none" stroke="var(--blue)" stroke-width="2"/></svg>Commercial</li>
    <li><svg viewBox="0 0 20 20"><circle cx="10" cy="10" r="8" fill="none" stroke="var(--blue)" stroke-width="2"/><path d="M6 10l3 3 6-6" fill="none" stroke="var(--blue)" stroke-width="2"/></svg>Curbside</li>
    <li><svg viewBox="0 0 20 20"><circle cx="10" cy="10" r="8" fill="none" stroke="var(--blue)" stroke-width="2"/><path d="M6 10l3 3 6-6" fill="none" stroke="var(--blue)" stroke-width="2"/></svg>Outside</li>
  </ul>
  <p class="abs band-title clean">CLEAN IT UP</p>
  <p class="abs band-title others">OTHERS</p>
  <p class="abs more">We're more than just junk.Capitalizing on our years<br>of experience we can work directly with you on a<br>Multitude of projects around your house.</p>
  <ul class="abs extras">
    <li>Donation pickup</li>
    <li>Mulch, gravel and topsoil delivery</li>
    <li>Packing and prepping for your move</li>
    <li>Loading/unloading your rental truck or POD</li>
  </ul>
  <p class="abs estimate">FREE ESTIMATE</p>
</section>

</body>
</html>
```